Business Identity Stationary

Already have the logo which is in the attached files so only need the Business STationary
1) Double Sided Business Card
2) Letterhead
3) Presentation folder with business card holder on inside cover
4) WIth compliments slip
See information for business cards, letterhead and presentation folder below.

This should be a simply job using a logo we already had designed along with a little device. I suggest using the device off center and perhaps lower in the corner in an abstract way. Also the logo device could be used as a watermark for the letterhead. The designer who created the logo presented something that I think works well for a business card. The front of the double sided business card could have the name logo small for the website address and only use the Lime device on the front. Then on the back could be the name Parvel Advisory logo.

Please note that for the business card the black and lime green background do look good. Also please think of using the lime device separately in an unusual way.

It has been brought to my attention that.my budget was far to low. Hopefully this.will attract you to the project. 

The parent company of Parvel Advisory is BrightHeron holdings. I have uploaded a file of the Bright Heron business card I really like. Perhaps use this business card as a guide to the type of modern and clean style I am looking for. It also works to have the Parvel Advisroy and Bright Heron similar.

Industry/Entity Type

Business

Font styles to use
Sans Serif

Colors
9bcb3c
000000
5c5c5c
add136
cadf82
eaf2cf
f9fbf2
1b1b1b
757575

Requirements
Must have
• 1) Double Sided Business Card
Renata Tolberg
Director
Tel: +505 8426 3057
Email: rtb@parveladvisory.com
Website: www.parveladvisory.com

Gregory Tolberg
Director
Tel: +505 8426 3092
Email: gkb@parveladvisory.com

Helena Pardo Duvignac
Director
Tel: 8342 1168
Email: hpd@parveladvisory.com

2) Letterhead
Logo
Lime Logo Device
Website Address: www.parveladvisory.com
Small print on bottom: Parvel Advisory a Bright Heron Holding Company SA. RUC K0470000283914

3) Presentation Folder
Traditional Presentation folder with inside front cover spot for the insertion of business card.

4) With Compliments slip

```html
<!DOCTYPE html>
<html lang="en">
<head>
<meta charset="utf-8">
<title>Parvel Advisory – Business Stationery</title>
<link href="https://fonts.googleapis.com/css2?family=Jost:wght@400;500&family=Pinyon+Script&display=swap" rel="stylesheet">
<style>
:root{
  --lime:#9bcb3c;
  --lime-soft:#add136;
  --lime-dark:#5f7f22;
  --ink:#1b1b1b;
  --grey:#757575;
  --grey-dark:#5c5c5c;
  --card-grey:#dcdedb;
  --paper:#ffffff;
  --folder:#f9fbf2;
  --backdrop:#efefef;
  --sans:'Jost', Arial, sans-serif;
}
*{margin:0;padding:0;box-sizing:border-box}
html,body{width:1200px;height:763px;overflow:hidden}
body{background:var(--backdrop);font-family:var(--sans);color:var(--ink);position:relative}
.abs{position:absolute}

/* wordmark */
.wordmark{display:flex;align-items:center;gap:.35em;font-family:var(--sans);font-weight:400;color:var(--ink);white-space:nowrap;letter-spacing:.02em}
.wordmark .dot{width:.55em;height:.55em;border-radius:50%;background:var(--lime);flex:none}

/* folder */
.folder-panel{background:var(--folder);box-shadow:0 2px 6px rgba(0,0,0,.12)}
.folder-left{left:32px;top:102px;width:356px;height:512px}
.folder-right{left:388px;top:94px;width:366px;height:512px;border-left:2px solid #e2e6d6}
.pocket{background:var(--lime);border-radius:6px 6px 0 0;box-shadow:0 -2px 4px rgba(0,0,0,.1)}
.pocket-left{left:36px;top:410px;width:358px;height:202px}
.pocket-right{left:398px;top:404px;width:354px;height:200px}
.folder-logo{left:500px;top:178px;font-size:30px}

/* business cards */
.card{width:146px;height:92px;box-shadow:0 2px 5px rgba(0,0,0,.22);overflow:hidden}
.card-front{background:var(--card-grey)}
.card-front .wordmark{position:absolute;left:50%;top:40%;transform:translate(-50%,-50%);font-size:11px}
.card-front .base{position:absolute;left:0;right:0;bottom:0;height:7px;background:var(--grey)}
.card-front .corner{position:absolute;left:0;bottom:0;width:7px;height:7px;background:var(--lime)}
.card-back{background:var(--paper);border-top:3px solid var(--lime);padding:8px 10px}
.card-back .name{font-size:7px;color:var(--lime);font-style:italic;margin-bottom:6px}
.card-back .row{display:flex;font-size:5.5px;color:var(--grey-dark);border-bottom:1px solid #ccc;line-height:10px}
.card-back .row span:first-child{width:28px;border-right:1px solid #ccc;margin-right:4px}
.card-back .mark{position:absolute;right:8px;top:8px;width:8px;height:8px;border-radius:50%;background:var(--lime)}
.card-white{background:var(--paper)}
.card-white .wordmark{position:absolute;left:50%;top:50%;transform:translate(-50%,-50%);font-size:11px}

/* letterhead */
.sheet{background:var(--paper);box-shadow:0 1px 4px rgba(0,0,0,.15);border-top:4px solid var(--lime)}
.sheet-back2{left:800px;top:148px;width:354px;height:500px}
.sheet-back1{left:796px;top:156px;width:354px;height:498px}
.letterhead{left:790px;top:162px;width:356px;height:494px;border-left:5px solid var(--lime)}
.letterhead-logo{left:930px;top:186px;font-size:24px}
.letterhead-foot{left:795px;top:636px;width:328px;height:16px;background:var(--grey);color:#fff;font-size:6px;display:flex;justify-content:space-between;align-items:center;padding:0 10px}
.letterhead-foot .accent{position:absolute;right:-22px;top:0;width:22px;height:16px;background:var(--lime)}

/* compliments slip */
.slip{left:762px;top:226px;width:332px;height:176px;background:var(--paper);box-shadow:0 2px 6px rgba(0,0,0,.2);border-top:2px solid var(--lime)}
.slip-title{left:20px;top:14px;font-family:'Pinyon Script',cursive;font-size:17px;color:var(--ink)}
.slip-contact{right:20px;bottom:22px;text-align:right;font-size:6.5px;line-height:10px;font-weight:500}
.slip-base{left:0;bottom:0;width:100%;height:5px;background:var(--grey)}
.slip-base::after{content:"";position:absolute;right:0;top:0;width:8px;height:5px;background:var(--lime)}

/* envelope */
.envelope{left:838px;top:420px;width:336px;height:158px;background:var(--lime);box-shadow:0 3px 7px rgba(0,0,0,.22)}
.envelope-logo{left:20px;top:12px;background:var(--lime-dark);padding:4px 6px;font-size:14px}
.envelope-logo .wordmark{color:#e9f2cf}
.envelope-tab{right:-2px;top:62px;width:34px;height:30px;background:var(--paper);border-radius:15px 0 0 15px}
</style>
</head>
<body>

<!-- presentation folder -->
<div class="abs folder-panel folder-left"></div>
<div class="abs folder-panel folder-right"></div>
<div class="abs folder-logo wordmark"><span class="dot"></span>Parvel Advisory</div>

<div class="abs pocket pocket-left">
  <svg width="358" height="202" viewBox="0 0 358 202" aria-hidden="true">
    <path d="M92 78 Q150 40 188 62 Q198 84 214 62 Q252 40 312 78" fill="none" stroke="#7fa82e" stroke-width="1.5"/>
  </svg>
</div>
<div class="abs pocket pocket-right">
  <svg width="354" height="200" viewBox="0 0 354 200" aria-hidden="true">
    <line x1="66" y1="64" x2="94" y2="36" stroke="#6d8f27" stroke-width="2"/>
    <line x1="214" y1="128" x2="242" y2="100" stroke="#6d8f27" stroke-width="2"/>
  </svg>
</div>
<div class="abs card card-white" style="left:496px;top:458px">
  <div class="wordmark"><span class="dot"></span>Parvel Advisory</div>
</div>

<!-- business cards -->
<div class="abs card card-front" style="left:92px;top:152px">
  <div class="wordmark"><span class="dot"></span>Parvel Advisory</div>
  <div class="base"></div><div class="corner"></div>
</div>
<div class="abs card card-back" style="left:196px;top:210px">
  <span class="mark"></span>
  <p class="name">Gregory Tolberg, Director</p>
  <div class="row"><span>Tel</span><span>+505 8426 3092</span></div>
  <div class="row"><span>Email</span><span>gkb@parveladvisory.com</span></div>
  <div class="row"><span>Website</span><span>www.parveladvisory.com</span></div>
</div>
<div class="abs card card-front" style="left:256px;top:612px">
  <div class="wordmark"><span class="dot"></span>Parvel Advisory</div>
  <div class="base"></div><div class="corner"></div>
</div>
<div class="abs card card-back" style="left:588px;top:590px;height:100px">
  <span class="mark"></span>
  <p class="name">Renata Tolberg, Director</p>
  <div class="row"><span>Tel</span><span>+505 8426 3057</span></div>
  <div class="row"><span>Email</span><span>rtb@parveladvisory.com</span></div>
  <div class="row"><span>Website</span><span>www.parveladvisory.com</span></div>
</div>

<!-- letterhead -->
<div class="abs sheet sheet-back2"></div>
<div class="abs sheet sheet-back1"></div>
<div class="abs sheet letterhead"></div>
<div class="abs letterhead-logo wordmark"><span class="dot"></span>Parvel Advisory</div>
<div class="abs letterhead-foot">
  <span>Parvel Advisory a Bright Heron Holding Company SA.</span>
  <span>www.parveladvisory.com</span>
  <span class="accent"></span>
</div>

<!-- compliments slip -->
<div class="abs slip">
  <p class="abs slip-title">With Compliments</p>
  <p class="abs slip-contact">Tel: +505 8426 3092<br>Email: info@parveladvisory.com</p>
  <div class="abs slip-base"></div>
</div>

<!-- envelope -->
<div class="abs envelope">
  <div class="abs envelope-logo"><div class="wordmark">Parvel Advisory</div></div>
  <div class="abs envelope-tab"></div>
</div>

</body>
</html>
```